Calloway Dental Care

I need a nice business card design that is double sided. This is for a dental surgery. I have already had a logo designed and just need the business card put together.

It needs to be in a format such that I can make new business cards if new dentists begin working for me. Hence I need to be able to change the text in order to have new names written on new cards.

The front will have the following text:

Dr Tariq Mansour
B. Med. Sci. QBTU B.Dent. Brel. Uni

The logo will appear somewhere on the front. This is attached.

In addition will be the following writing that also needs to appear on the front of the card, perhaps at the bottom on the left side will be:

Shop 4, 212-240 Parlow Street, North Sydney, NSW, 2060

and at the bottom on the right side will be:
(02) 5550 1736
e: info@callowaydentalcare.com.au
www.callowaydentalcare.com.au

On the back of the card will be a section for a map to be drawn (I have uploaded a picture) and also a section written as follows:

"Your next appointment is: (a line needs to be here to write date and time)"

Also I need two lines for two appointments to be written.

Thanks for your efforts!

```html
<!DOCTYPE html>
<html lang="en">
<head>
<meta charset="UTF-8">
<title>Calloway Dental Care – Business Card</title>
<link href="https://fonts.googleapis.com/css2?family=Artifika&display=swap" rel="stylesheet">
<style>
  :root {
    --backdrop: #e6e7e9;
    --card: #ffffff;
    --navy: #336aa1;
    --sky: #35c5f3;
    --white: #ffffff;
    --rule: #c8d5e2;
    --ghost: #eef1f6;
  }
  * { margin: 0; padding: 0; box-sizing: border-box; }
  html, body { width: 1200px; height: 1000px; overflow: hidden; }
  body {
    background: var(--backdrop);
    position: relative;
    font-family: "Artifika", Georgia, serif;
  }
  .card {
    position: absolute;
    width: 643px;
    height: 371px;
    background: var(--card);
    overflow: hidden;
  }
  .card--front { left: 100px; top: 94px; }
  .card--back { left: 457px; top: 535px; }

  .front-wave { position: absolute; inset: 0; }

  .brand {
    position: absolute;
    left: 48px;
    top: 96px;
    width: 170px;
    text-align: center;
    color: var(--navy);
  }
  .brand__dot {
    width: 34px; height: 34px;
    border-radius: 50%;
    background: var(--navy);
    margin: 0 auto 14px;
  }
  .brand__name { font-size: 30px; line-height: 1; letter-spacing: 0.5px; }
  .brand__sub { font-size: 12px; letter-spacing: 3px; margin-top: 8px; }

  .dentist { position: absolute; left: 335px; top: 32px; }
  .dentist__name { font-size: 22px; font-weight: 700; color: var(--navy); letter-spacing: 0.3px; }
  .dentist__credentials { font-size: 15px; color: var(--sky); margin-top: 2px; }

  .address {
    position: absolute; left: 35px; top: 302px;
    color: var(--white); font-size: 14px; line-height: 20px;
  }
  .contact {
    position: absolute; left: 356px; top: 302px;
    color: var(--white); font-size: 14px; line-height: 20px;
    list-style: none;
  }
  .contact li { display: flex; align-items: center; gap: 6px; }
  .contact svg { width: 14px; height: 12px; flex: none; }

  .ghost-brand {
    position: absolute; left: 0; right: 0; top: 150px;
    text-align: center; color: var(--ghost);
  }
  .ghost-brand__dot {
    width: 90px; height: 90px; border-radius: 50%;
    background: var(--ghost); margin: -100px auto 20px;
  }
  .ghost-brand__name { font-size: 62px; line-height: 1; }
  .ghost-brand__sub { font-size: 20px; letter-spacing: 8px; margin-top: 10px; }

  .appointment__title {
    position: absolute; left: 0; right: 0; top: 44px;
    text-align: center; font-size: 19px; font-weight: 400;
    color: var(--navy); text-decoration: underline; text-underline-offset: 3px;
  }
  .appointment__line {
    position: absolute; left: 36px; width: 567px;
    border-top: 1px solid var(--rule);
  }
</style>
</head>
<body>
  <section class="card card--front">
    <svg class="front-wave" viewBox="0 0 643 371" width="643" height="371" aria-hidden="true">
      <path d="M0,297 C200,278 370,225 470,180 C540,148 600,108 643,84 L643,371 L0,371 Z" fill="var(--sky)"/>
    </svg>

    <div class="brand">
      <div class="brand__dot"></div>
      <div class="brand__name">CALLOWAY</div>
      <div class="brand__sub">DENTAL CARE</div>
    </div>

    <div class="dentist">
      <h1 class="dentist__name">Dr Tariq Mansour</h1>
      <p class="dentist__credentials">B Med Sci (QBTU), BDent (Brel. Uni)</p>
    </div>

    <address class="address">
      Shop 4, 212-240 Parlow Street,<br>
      North Sydney, 2060
    </address>

    <ul class="contact">
      <li>
        <svg viewBox="0 0 14 14" aria-hidden="true"><path d="M3 1 L5.5 1 L6.5 4 L5 5.5 C5.8 7.5 6.8 8.6 8.5 9.5 L10 8 L13 9 L13 11.5 C13 12.5 12 13 11 13 C6 12.5 1.5 8 1 3 C1 2 2 1 3 1 Z" fill="var(--white)"/></svg>
        (02) 5550 1736
      </li>
      <li>
        <svg viewBox="0 0 14 10" aria-hidden="true"><rect x="0.5" y="0.5" width="13" height="9" fill="var(--white)"/><path d="M0.5 0.5 L7 5.5 L13.5 0.5" fill="none" stroke="var(--sky)" stroke-width="1"/></svg>
        info@callowaydentalcare.com.au
      </li>
    </ul>
  </section>

  <section class="card card--back">
    <div class="ghost-brand" aria-hidden="true">
      <div class="ghost-brand__dot"></div>
      <div class="ghost-brand__name">CALLOWAY</div>
      <div class="ghost-brand__sub">DENTAL CARE</div>
    </div>

    <h2 class="appointment__title">Your next appointment:</h2>
    <div class="appointment__line" style="top:124px"></div>
    <div class="appointment__line" style="top:183px"></div>
    <div class="appointment__line" style="top:243px"></div>
    <div class="appointment__line" style="top:302px"></div>
  </section>
</body>
</html>
```